White Dove Release Postcard for Event Planners

We require a double-sided Postcard (8.5" x 5.5") that will be mailed to Event Planners advising them of our White Dove Release services for weddings, anniversaries, and other happy events.

Wingfall Moments is the originator of White Dove Releases in the greater Toronto area, adding a beautiful moment to weddings and other celebrations since 1995.

A professional release of Pure White Doves is a natural part of wedding ceremonies, lending a special celebratory note to the exchange of vows. White Doves are the living symbol of everlasting love, fidelity, peace and harmony. These lovely birds mate for life, building a home and raising their young together.

For more information, please visit www.wingfallmoments.example

Target Market(s)

Event and Wedding Planners. Primarily for weddings but could be for other types of celebratory events.

Industry/Entity Type

Events

Requirements
Must have
• Space for address label and stamp to be affixed.
• Pictures of beautiful brides with doves (see attachments).
Nice to have
• Multicultural weddings / brides
Should not have
• No religious images. Must be non-denominational.

```html
<!DOCTYPE html>
<html lang="en">
<head>
<meta charset="utf-8">
<title>Wingfall Moments Postcard</title>
<link rel="stylesheet" href="https://fonts.googleapis.com/css2?family=Cinzel:wght@400;600;700&family=Open+Sans:ital@1&display=swap">
<style>
  :root {
    --backdrop: #5b5b5d;
    --ink: #000000;
    --paper: #ffffff;
    --rule: #a8a8a8;
    --accent: #f5b041;
    --photo-light: #bdbdbd;
    --photo-dark: #2a2a2a;
  }
  html, body {
    margin: 0;
    padding: 0;
    overflow: hidden;
  }
  .canvas {
    position: relative;
    width: 1160px;
    height: 1200px;
    background: var(--backdrop);
    overflow: hidden;
    font-family: "Cinzel", serif;
  }
  .card {
    position: absolute;
    box-sizing: border-box;
  }
  .card--front {
    left: 255px;
    top: 109px;
    width: 712px;
    height: 462px;
    background: var(--ink);
  }
  .front-photo {
    position: absolute;
    left: 0;
    top: 0;
    width: 397px;
    height: 462px;
    background: linear-gradient(135deg, var(--photo-light) 0%, #8a8a8a 40%, var(--photo-dark) 100%);
  }
  .front-panel {
    position: absolute;
    left: 397px;
    top: 0;
    width: 315px;
    height: 462px;
    color: var(--paper);
    text-align: center;
  }
  .front-panel .line {
    position: absolute;
    left: 0;
    width: 100%;
    margin: 0;
  }
  .studio-name {
    font-size: 15px;
    letter-spacing: 0.5px;
    font-weight: 400;
  }
  .front-panel .studio-name { top: 70px; }
  .headline {
    font-weight: 600;
    font-size: 38px;
    line-height: 42px;
    letter-spacing: 1px;
  }
  .front-panel .headline { top: 114px; }
  .front-ornament {
    position: absolute;
    left: 133px;
    top: 210px;
    width: 50px;
    height: 22px;
    background: #d9d9d9;
  }
  .services-list {
    font-size: 14px;
    font-weight: 600;
    letter-spacing: 0.4px;
  }
  .front-panel .services-list { top: 246px; line-height: 25.5px; }
  .front-divider {
    position: absolute;
    left: 118px;
    top: 333px;
    width: 80px;
    height: 1px;
    background: #9a9a9a;
  }
  .region {
    font-size: 13px;
    font-weight: 600;
    letter-spacing: 0.5px;
  }
  .front-panel .region { top: 346px; line-height: 24px; }
  .web-address {
    font-family: "Open Sans", sans-serif;
    font-style: italic;
    font-size: 10px;
  }
  .front-panel .web-address { top: 427px; }

  .card--back {
    left: 252px;
    top: 636px;
    width: 712px;
    height: 461px;
    background: var(--paper);
    border: 1px solid #222;
  }
  .back-heading {
    position: absolute;
    left: 0;
    top: 42px;
    width: 528px;
    text-align: center;
    color: var(--ink);
  }
  .back-heading p { margin: 0; }
  .back-heading .studio-name { font-size: 15px; line-height: 20px; }
  .back-heading .headline { font-size: 37px; line-height: 44px; font-weight: 700; }
  .back-heading .services-inline { font-size: 13px; font-weight: 700; line-height: 22px; letter-spacing: 0.3px; }
  .back-heading .region { font-size: 13px; font-weight: 400; line-height: 20px; }
  .stamp-box {
    position: absolute;
    left: 577px;
    top: 43px;
    width: 88px;
    height: 105px;
    border: 1px solid #333;
    box-sizing: border-box;
  }
  .address-divider {
    position: absolute;
    left: 375px;
    top: 204px;
    width: 1px;
    height: 227px;
    background: var(--rule);
  }
  .address-lines {
    position: absolute;
    left: 399px;
    top: 255px;
    width: 269px;
    margin: 0;
    padding: 0;
    list-style: none;
  }
  .address-lines li {
    height: 33px;
    border-top: 1px solid var(--rule);
  }
  .dove-art {
    position: absolute;
    left: 121px;
    top: 184px;
    width: 203px;
    height: 240px;
    background: radial-gradient(ellipse at 55% 45%, #f4f4f4 0%, #e2e2e2 55%, rgba(255,255,255,0) 75%);
  }
  .corner-ornament {
    position: absolute;
    left: 28px;
    top: 327px;
    width: 107px;
    height: 101px;
    background: var(--accent);
    border-radius: 40% 55% 30% 45%;
  }
</style>
</head>
<body>
<div class="canvas">
  <section class="card card--front">
    <div class="front-photo" role="img" aria-label="Black and white photo of a bride and groom kissing while holding white doves"></div>
    <div class="front-panel">
      <p class="line studio-name">Silver Feather Works</p>
      <h1 class="line headline">WINGFALL<br>MOMENTS</h1>
      <div class="front-ornament" role="img" aria-label="Small white flourish ornament"></div>
      <p class="line services-list">Weddings<br>Life Celebrations<br>Private &amp; Public Events</p>
      <div class="front-divider"></div>
      <p class="line region">Serving Southern Ontario<br>Since 1995</p>
      <p class="line web-address">www.wingfallmoments.example</p>
    </div>
  </section>

  <section class="card card--back">
    <div class="back-heading">
      <p class="studio-name">Silver Feather Works</p>
      <h2 class="headline" style="margin:0">WINGFALL MOMENTS</h2>
      <p class="services-inline">Weddings • Life Celebrations • Private &amp; Public Events</p>
      <p class="region">Serving Southern Ontario Since 1995</p>
    </div>
    <div class="stamp-box"></div>
    <div class="address-divider"></div>
    <ul class="address-lines">
      <li></li><li></li><li></li><li></li><li></li><li></li>
    </ul>
    <div class="dove-art" role="img" aria-label="White dove in flight with wings raised"></div>
    <div class="corner-ornament" role="img" aria-label="Orange floral flourish ornament"></div>
  </section>
</div>
</body>
</html>
```